Business Card Re-design

We are looking for a fresh bold look for general office business cards. We are a staffing agency that staffs industrial, coal mining, and clerical jobs.
Tag Line: We connect the RIGHT people with the RIGHT jobs.
Evansville Office: 2473 W. Tallow Creek Rd, Evansville, IN - 47308
p. 555.203.6180 f. 555.203.6195
Princeton Office: 264 S. Birch Ln, Princeton, IN - 47152
p. 555.319.2047 f. 555.203.6195
Absentee/Emergency 24hr Hotline 555.203.6172 opt.1
www.bluelanternworkforce.example

```html
<!DOCTYPE html>
<html lang="en">
<head>
<meta charset="utf-8">
<title>Blue Lantern Workforce – Business Cards</title>
<link rel="stylesheet" href="https://fonts.googleapis.com/css2?family=Open+Sans:wght@400;600;700&display=swap">
<style>
  :root {
    --navy: #15253f;
    --green: #2f9a40;
    --ink: #333333;
    --white: #ffffff;
    --backdrop: #e9e9e9;
  }
  * { box-sizing: border-box; margin: 0; padding: 0; }
  html, body { width: 1200px; height: 976px; overflow: hidden; }
  body {
    background: var(--backdrop);
    font-family: "Open Sans", Arial, sans-serif;
    position: relative;
  }
  .card {
    position: absolute;
    top: 314px;
    width: 570px;
    height: 347px;
    box-shadow: 0 4px 14px rgba(0,0,0,0.18);
    overflow: hidden;
  }
  .card--evansville { left: 15px; background: var(--white); }
  .card--princeton { left: 615px; background: var(--navy); }
  .card__shape { position: absolute; inset: 0; width: 570px; height: 347px; }

  .office-title {
    position: absolute;
    left: 40px; top: 70px;
    font-weight: 700;
    font-size: 25px;
    line-height: 24px;
    letter-spacing: -0.2px;
    color: var(--ink);
  }
  .card--princeton .office-title { color: var(--white); }

  .hotline {
    position: absolute;
    left: 338px; top: 73px;
    font-size: 11px;
    line-height: 13px;
    color: var(--ink);
  }
  .card--princeton .hotline { color: var(--white); }
  .hotline__number {
    display: block;
    margin-top: 3px;
    font-size: 14px;
    font-weight: 700;
    color: var(--green);
  }

  .contact {
    position: absolute;
    left: 34px; top: 186px;
    list-style: none;
    color: var(--white);
    font-size: 14.5px;
    line-height: 21.5px;
  }
  .contact li { display: flex; align-items: flex-start; }
  .contact__icon { width: 12px; height: 12px; margin: 5px 16px 0 0; flex: none; }
  .contact__icon--blank { visibility: hidden; }

  .brand-name {
    position: absolute;
    left: 404px; top: 212px;
    font-weight: 700;
    font-size: 21px;
    line-height: 28px;
    color: var(--navy);
  }

  .tagline {
    position: absolute;
    left: 0; right: 0; top: 324px;
    text-align: center;
    font-size: 11px;
    color: var(--ink);
  }
  .card--princeton .tagline { color: var(--white); }
</style>
</head>
<body>

<svg width="0" height="0" style="position:absolute">
  <defs>
    <symbol id="icon-home" viewBox="0 0 12 12"><path d="M6 1 L11.5 6 H10 V11 H7.3 V8 H4.7 V11 H2 V6 H0.5 Z" fill="#2f9a40"/></symbol>
    <symbol id="icon-phone" viewBox="0 0 12 12"><path d="M2.5 1 L4.5 1 L5.3 3.6 L4 4.6 Q5 7 7.4 8 L8.4 6.7 L11 7.5 L11 9.5 Q10.5 11 9 11 Q1 10 1 3 Q1 1.5 2.5 1 Z" fill="#2f9a40"/></symbol>
    <symbol id="icon-fax" viewBox="0 0 12 12"><rect x="3" y="1" width="6" height="3" fill="#2f9a40"/><rect x="1" y="4.5" width="10" height="4.5" rx="1" fill="#2f9a40"/><rect x="3" y="8" width="6" height="3" fill="#2f9a40"/></symbol>
    <symbol id="icon-web" viewBox="0 0 12 12"><circle cx="6" cy="6" r="5" fill="none" stroke="#2f9a40" stroke-width="1.4"/><path d="M1 6 H11 M6 1 Q3 6 6 11 M6 1 Q9 6 6 11" fill="none" stroke="#2f9a40" stroke-width="1"/></symbol>
  </defs>
</svg>

<section class="card card--evansville" aria-label="Evansville office business card">
  <svg class="card__shape" viewBox="0 0 570 347" aria-hidden="true">
    <polygon points="0,169 447,169 304,317 0,317" fill="#15253f"/>
  </svg>
  <h2 class="office-title">EVANSVILLE<br>OFFICE</h2>
  <p class="hotline">Absentee/<br>Emergency 24hr Hotline<span class="hotline__number">555.203.6172 opt.1</span></p>
  <ul class="contact">
    <li><svg class="contact__icon"><use href="#icon-home"/></svg>2473 W. Tallow Creek Rd,</li>
    <li><svg class="contact__icon contact__icon--blank"></svg>Evansville, IN - 47308</li>
    <li><svg class="contact__icon"><use href="#icon-phone"/></svg>555.203.6180</li>
    <li><svg class="contact__icon"><use href="#icon-fax"/></svg>555.203.6195</li>
    <li><svg class="contact__icon"><use href="#icon-web"/></svg>www.bluelanternworkforce.example</li>
  </ul>
  <p class="brand-name">BLUE<br>LANTERN<br>WORKFORCE</p>
  <p class="tagline">We connect the RIGHT people with the RIGHT jobs.</p>
</section>

<section class="card card--princeton" aria-label="Princeton office business card">
  <svg class="card__shape" viewBox="0 0 570 347" aria-hidden="true">
    <polygon points="448,169 570,169 570,317 303,317" fill="#ffffff"/>
  </svg>
  <h2 class="office-title">PRINCETON<br>OFFICE</h2>
  <p class="hotline">Absentee/<br>Emergency 24hr Hotline<span class="hotline__number">555.203.6172 opt.1</span></p>
  <ul class="contact">
    <li><svg class="contact__icon"><use href="#icon-home"/></svg>264 S. Birch Ln, Princeton,</li>
    <li><svg class="contact__icon contact__icon--blank"></svg>IN - 47152</li>
    <li><svg class="contact__icon"><use href="#icon-phone"/></svg>555.319.2047</li>
    <li><svg class="contact__icon"><use href="#icon-fax"/></svg>555.203.6195</li>
    <li><svg class="contact__icon"><use href="#icon-web"/></svg>www.bluelanternworkforce.example</li>
  </ul>
  <p class="brand-name">BLUE<br>LANTERN<br>WORKFORCE</p>
  <p class="tagline">We connect the RIGHT people with the RIGHT jobs.</p>
</section>

</body>
</html>
```